Fern Vale Accounting - New client package

I need a stationary package (presentation folder cover, welcome letter template/design, sample financial report template/design, business card and new logo) for my accounting business. I would like to see designs that use the color blue. Financial icons can be included in the design. The final design should be clean and communicate professionalism and the use of modern; user-friendly technology. Attached postcard files should help with overall design concept.

```html
<!DOCTYPE html>
<html lang="en">
<head>
<meta charset="utf-8">
<title>Fern Vale Accounting – Business Card</title>
<link rel="stylesheet" href="https://fonts.googleapis.com/css2?family=Arimo:wght@400;700&display=swap">
<style>
  :root {
    --navy: #004a8c;
    --sky: #1a8fd0;
    --ink: #3a3f45;
    --paper: #ffffff;
    --backdrop: #dfe3e5;
  }
  * { box-sizing: border-box; margin: 0; padding: 0; }
  html, body { width: 1200px; height: 906px; overflow: hidden; }
  body {
    background: var(--backdrop);
    font-family: "Arimo", Arial, sans-serif;
    position: relative;
  }
  .card {
    position: absolute;
    left: 260px;
    width: 680px;
    height: 389px;
    overflow: hidden;
    box-shadow: 0 6px 18px rgba(0,0,0,0.12);
  }
  .card--front { top: 42px; background: var(--navy); }
  .card--back { top: 475px; background: var(--paper); }

  .brand {
    display: flex;
    align-items: center;
    gap: 16px;
  }
  .brand__mark { width: 40px; height: 40px; flex: none; }
  .brand__name {
    font-weight: 400;
    text-transform: uppercase;
    letter-spacing: 0.12em;
    line-height: 1.05;
    font-size: 22px;
  }
  .card--front .brand {
    position: absolute;
    left: 50%; top: 50%;
    transform: translate(-50%, -50%);
  }
  .card--front .brand__mark { background: var(--sky); }
  .card--front .brand__name { color: var(--paper); }

  .card--back .brand { position: absolute; left: 60px; top: 112px; }
  .card--back .brand__mark { background: var(--sky); width: 34px; height: 34px; }
  .card--back .brand__name { color: var(--navy); font-size: 19px; }

  .holder { position: absolute; right: 56px; top: 44px; text-align: right; }
  .holder__name { color: var(--navy); font-weight: 700; font-size: 20px; letter-spacing: 0.01em; }
  .holder__role { color: var(--ink); font-size: 13px; margin-top: 4px; }

  .address {
    position: absolute; right: 56px; top: 230px;
    text-align: right; color: var(--ink); font-size: 13px; line-height: 1.5;
  }

  .contacts { position: absolute; left: 60px; top: 262px; list-style: none; }
  .contacts li {
    display: flex; align-items: center; gap: 10px;
    color: var(--ink); font-size: 13px; line-height: 22px;
  }
  .contacts svg { width: 13px; height: 13px; flex: none; }

  .bands { position: absolute; left: 0; bottom: 0; width: 680px; height: 36px; }
</style>
</head>
<body>
  <section class="card card--front" aria-label="Business card front">
    <div class="brand">
      <span class="brand__mark"></span>
      <span class="brand__name">Fern Vale<br>Accounting</span>
    </div>
  </section>

  <section class="card card--back" aria-label="Business card back">
    <div class="brand">
      <span class="brand__mark"></span>
      <span class="brand__name">Fern Vale<br>Accounting</span>
    </div>

    <div class="holder">
      <p class="holder__name">JORDAN ELLERY</p>
      <p class="holder__role">General Manager</p>
    </div>

    <p class="address">Level 12, Harbour Point<br>18 Kent Lane, Sydney</p>

    <ul class="contacts">
      <li>
        <svg viewBox="0 0 16 16" aria-hidden="true"><path fill="#004a8c" d="M3.5 1l2.5 3-1.5 2c.8 2 2.5 3.7 4.5 4.5l2-1.5 3 2.5-1.5 2.5C7 14 2 9 1 2.5z"/></svg>
        305-555-0148
      </li>
      <li>
        <svg viewBox="0 0 16 16" aria-hidden="true"><rect x="1" y="3" width="14" height="10" fill="#004a8c"/><path d="M1.5 3.5L8 9l6.5-5.5" stroke="#fff" stroke-width="1.4" fill="none"/></svg>
        info@fernvaleaccounting.com
      </li>
      <li>
        <svg viewBox="0 0 16 16" aria-hidden="true"><g fill="none" stroke="#004a8c" stroke-width="1.3"><circle cx="8" cy="8" r="6.5"/><ellipse cx="8" cy="8" rx="3" ry="6.5"/><path d="M1.5 8h13M2.5 4.8h11M2.5 11.2h11"/></g></svg>
        www.fernvaleaccounting.com
      </li>
    </ul>

    <svg class="bands" viewBox="0 0 680 36" aria-hidden="true">
      <polygon points="0,28 395,28 392,36 0,36" fill="#1a8fd0"/>
      <polygon points="412,18 680,0 680,36 402,36" fill="#004a8c"/>
    </svg>
  </section>
</body>
</html>
```